Webdesign für Verkauf von Stoffen
Zielgruppe
Palmtuche ist schon seit 15 Jahren auf den Märkten unterwegs und verkauft seine hochwertigen Stoffe vor Ort. Nun muss die Webseite ein neuen Look bekommen, sie sollte modern und locker wirken. Die Webseite ist eher für Privatkunden und hat jetzt noch keine Shop Möglichkeit, die wird aber intrigiert mit einzelnen Produkten.
Aufgabenstellung
Logo gibt es noch nicht, soll erstmal nur in Schriftform bleiben, ansonsten gibt es keine explizierten Vorgaben

```html
<!DOCTYPE html>
<html lang="de">
<head>
<meta charset="utf-8">
<title>Palmtuche – Feiner Zwirn</title>
<link rel="stylesheet" href="https://fonts.googleapis.com/css2?family=Playfair+Display:wght@400&family=Open+Sans:wght@400;600&display=swap">
<style>
  :root {
    --purple: #7d2f8c;
    --purple-deep: #2a0f33;
    --silk-a: #3b1448;
    --silk-b: #8a3aa6;
    --panel-gray: #8e8e8e;
    --text-gray: #6e6c70;
    --band-gray: #676367;
    --white: #ffffff;
    --ink: #111111;
    --input-line: #4a4a4a;
    --button: #c9a7a7;
    --strip: #ececec;
  }
  * { margin: 0; padding: 0; box-sizing: border-box; }
  html, body { width: 1200px; height: 3990px; overflow: hidden; background: var(--white); }
  body { position: relative; font-family: "Open Sans", Arial, sans-serif; color: var(--text-gray); }
  .block, .photo { position: absolute; }
  .serif { font-family: "Playfair Display", Georgia, serif; font-weight: 400; }

  /* Hero */
  .hero { left: 0; top: 0; width: 1200px; height: 416px;
    background: radial-gradient(ellipse at 70% 40%, var(--silk-b) 0%, var(--silk-a) 55%, var(--purple-deep) 100%); }
  .main-nav { position: absolute; top: 24px; left: 582px; display: flex; gap: 46px; font-size: 21px; color: var(--white); }
  .brand-name, .brand-line { position: absolute; font-size: 46px; line-height: 1; color: var(--white); white-space: nowrap; }
  .brand-name { left: 436px; top: 208px; }
  .brand-line { left: 292px; top: 262px; }

  /* Fashion */
  .runway-photo { left: 0; top: 416px; width: 739px; height: 818px;
    background: linear-gradient(180deg, #3a3a3a 0%, #9a9a9a 45%, #e0e0e0 100%); }
  .quote-panel { left: 739px; top: 416px; width: 461px; height: 818px; background: var(--panel-gray); }
  .quote { position: absolute; left: 646px; top: 448px; font-size: 92px; line-height: 110px; color: var(--white); }

  /* Products */
  .range-box { left: 0; top: 1268px; width: 596px; height: 270px; background: var(--purple); color: var(--white); }
  .range-box h2 { position: absolute; left: 40px; top: 24px; font-weight: 400; font-size: 32px; }
  .range-list { position: absolute; left: 228px; top: 84px; list-style: none; font-size: 14px; line-height: 31px; }
  .linen-photo { left: 596px; top: 1268px; width: 604px; height: 700px;
    background: linear-gradient(135deg, #e2d9cc 0%, #cdbfad 50%, #e8e0d4 100%); }
  .claim { position: absolute; left: 30px; top: 1570px; font-size: 90px; line-height: 101px; color: var(--text-gray); }

  /* Fabric row */
  .fabric-satin { left: 0; top: 1985px; width: 400px; height: 483px; background: linear-gradient(135deg, #3b3a1c 0%, #8e8a4a 50%, #2c2b14 100%); }
  .fabric-geo { left: 400px; top: 1985px; width: 400px; height: 483px; background: linear-gradient(135deg, #20283a 0%, #c9a46a 50%, #e8dcc0 100%); }
  .fabric-leo { left: 800px; top: 1985px; width: 400px; height: 483px; background: linear-gradient(135deg, #c88a4c 0%, #a4632e 50%, #d9a468 100%); }

  /* Text band */
  .story { left: 0; top: 2480px; width: 1200px; height: 248px; background: var(--band-gray); color: var(--white); padding: 36px 26px; font-size: 14px; line-height: 23px; }

  /* Contact */
  .contact-title { position: absolute; left: 58px; top: 2745px; font-size: 90px; line-height: 1.1; color: var(--ink); }
  .contact-form { position: absolute; left: 58px; top: 2935px; width: 530px; }
  .contact-form h3 { font-weight: 400; font-size: 29px; color: var(--ink); margin-bottom: 180px; }
  .field { display: block; width: 530px; height: 44px; border: 1.5px solid var(--input-line); background: var(--white); margin-bottom: 30px; }
  .field.message { height: 118px; margin-bottom: 40px; }
  .send { display: block; width: 110px; height: 40px; background: var(--button); color: var(--white); font-size: 14px; line-height: 40px; text-align: center; }
  .tea-photo { left: 612px; top: 2897px; width: 560px; height: 768px;
    background: linear-gradient(160deg, #f6eee8 0%, #f2c8b0 50%, #faf5f0 100%); }

  /* Footer */
  .site-footer { left: 0; top: 3709px; width: 1200px; height: 226px; background: var(--purple); color: var(--white); text-align: center; font-size: 13px; line-height: 21px; padding-top: 62px; }
  .legal-strip { left: 0; top: 3935px; width: 1200px; height: 55px; background: var(--strip); color: #888; text-align: center; font-size: 13px; line-height: 55px; }
</style>
</head>
<body>

<header class="block hero" role="img" aria-label="Violetter Seidenstoff in weichen Falten">
  <nav class="main-nav"><span>Startseite</span><span>Produkte</span><span>Über uns</span><span>Kontakt</span></nav>
  <span class="brand-name serif">Palmtuche</span>
  <span class="brand-line serif">Feiner Zwirn</span>
</header>

<div class="photo runway-photo" role="img" aria-label="Models auf dem Laufsteg in eleganter Kleidung"></div>
<div class="block quote-panel"></div>
<h1 class="quote serif">Eleganz<br>kommt nie<br>aus der<br>Mode</h1>

<section class="block range-box">
  <h2>Produktpalette</h2>
  <ul class="range-list">
    <li>Leinenstoffe</li>
    <li>100% Leinen Meterware</li>
    <li>Seide &amp; Satin</li>
    <li>Samt &amp; Velour</li>
    <li>u.v.m.</li>
  </ul>
</section>
<div class="photo linen-photo" role="img" aria-label="Nahaufnahme von naturfarbenem Leinenstoff"></div>
<h2 class="claim serif">Hochwertige<br>Stoffe aus<br>aller Welt</h2>

<div class="photo fabric-satin" role="img" aria-label="Olivgrüner glänzender Satinstoff"></div>
<div class="photo fabric-geo" role="img" aria-label="Stoff mit geometrischem Muster in Blau und Gold"></div>
<div class="photo fabric-leo" role="img" aria-label="Stoff mit Leopardenmuster"></div>

<section class="block story">
  <p>Wir verkaufen seit fünfzehn Jahren hochwertige Stoffe auf Märkten in der ganzen Region. Bei uns finden Sie eine sorgfältig ausgewählte Auswahl an Leinen, Seide, Samt und Baumwolle, die wir direkt von ausgesuchten Webereien aus aller Welt beziehen. Jeder Stoff wird von uns geprüft, bevor er in unser Sortiment aufgenommen wird, damit Sie lange Freude an Ihren Projekten haben.</p>
  <p>Ob Kleid, Vorhang, Kissen oder Tischdecke: Unsere Stoffe eignen sich für Hobbynäherinnen ebenso wie für erfahrene Schneider. Gerne beraten wir Sie persönlich am Stand oder per Nachricht zu Farben, Materialien und Pflege. Bald können Sie ausgewählte Produkte auch bequem online bestellen. Besuchen Sie uns auf dem nächsten Markt und lassen Sie sich von der Vielfalt unserer Muster und Qualitäten inspirieren. Wir freuen uns auf Sie und Ihre Ideen.</p>
</section>

<h2 class="contact-title serif">Kontaktiere uns</h2>
<form class="contact-form">
  <h3>Schreib uns</h3>
  <span class="field"></span>
  <span class="field"></span>
  <span class="field message"></span>
  <span class="send">Senden</span>
</form>
<div class="photo tea-photo" role="img" aria-label="Teetasse, Gebäck, Blütenblätter und ein offenes Buch"></div>

<footer class="block site-footer">
  <p>Palmtuche GmbH</p>
  <p>Ahornweg 12 · 40210 Musterstadt</p>
  <p>Telefon 0211 4455667 · info@palmtuche.de · Mo–Fr 9–18 Uhr</p>
  <p>Impressum · Datenschutz</p>
</footer>
<div class="block legal-strip">© 2024 Palmtuche · Alle Rechte vorbehalten</div>

</body>
</html>
```